Visitenkarten
Zielgruppe
Wir handeln und restaurieren (mit) sehr hochwertigen Fahrzeugen (Oldtimier/Supercars) bis in den Bereich von mehreren Millionen Euro. Die Zielgruppe sind potentielle Käufer im sehr gehobenen Premium Segment.
Aufgabenstellung
Eine Visitenkarte im Idealfall mit dem schwarzen Logo soll erstellt werden. Standardformat oder ein kreatives, aber praktikables Format. Ziel ist eine sehr hochwertige, geprägte Visitenkarte. Frontseite das Vintage Crest Logo, Rückseite einmal: Markus Wendler, Owner, Phone +436701927468, Email Sales@vintage-crest-autos.example Salzburg Dobrovnik (generisch anpassbare Adresse)

```html
<!DOCTYPE html>
<html lang="de">
<head>
<meta charset="utf-8">
<title>Vintage Crest – Visitenkarten</title>
<link rel="stylesheet" href="https://fonts.googleapis.com/css2?family=Poppins:wght@400;700&display=swap">
<style>
  :root {
    --ink: #000000;
    --paper: #f2f2f2;
    --gold: #c0922e;
    --text-dark: #111111;
    --text-light: #ececec;
    --backdrop: #e6e6e4;
  }
  html, body {
    margin: 0;
    padding: 0;
    width: 1200px;
    height: 1058px;
    overflow: hidden;
    background: var(--backdrop);
    font-family: "Poppins", sans-serif;
  }
  .stage {
    position: relative;
    width: 1200px;
    height: 1058px;
  }
  .card {
    position: absolute;
    top: 354px;
    width: 540px;
    height: 350px;
    overflow: hidden;
    box-shadow: 0 10px 30px rgba(0,0,0,0.18);
  }
  /* front */
  .card-front {
    left: 30px;
    background: var(--ink);
    display: flex;
    align-items: center;
    justify-content: center;
  }
  .front-mark {
    display: flex;
    align-items: center;
    gap: 18px;
  }
  .front-mark .dot {
    width: 26px;
    height: 26px;
    border-radius: 50%;
    background: var(--gold);
  }
  .front-mark .name {
    color: var(--text-light);
    font-weight: 400;
    font-size: 44px;
    letter-spacing: 0.08em;
    text-transform: uppercase;
  }
  /* back */
  .card-back {
    left: 630px;
    background: var(--paper);
  }
  .back-panel {
    position: absolute;
    left: 0;
    top: 0;
    width: 214px;
    height: 100%;
    background: var(--ink);
    display: flex;
    align-items: center;
    justify-content: center;
  }
  .back-panel .name {
    color: var(--text-light);
    font-weight: 400;
    font-size: 17px;
    letter-spacing: 0.1em;
    text-transform: uppercase;
  }
  .gold-bar {
    position: absolute;
    left: 214px;
    top: 34px;
    width: 12px;
    bottom: 0;
    background: var(--gold);
  }
  .contact {
    position: absolute;
    left: 268px;
    top: 58px;
    color: var(--text-dark);
  }
  .person {
    margin: 0;
    font-weight: 700;
    font-size: 25px;
    line-height: 1.02;
    text-transform: uppercase;
    letter-spacing: 0.02em;
  }
  .role {
    margin: 8px 0 0 0;
    font-weight: 700;
    font-size: 13px;
    text-transform: uppercase;
    letter-spacing: 0.04em;
  }
  .details {
    list-style: none;
    margin: 40px 0 0 0;
    padding: 0;
    font-size: 13px;
    font-weight: 400;
    line-height: 2.2;
  }
</style>
</head>
<body>
  <main class="stage">
    <section class="card card-front" aria-label="Vorderseite">
      <div class="front-mark">
        <span class="dot" aria-hidden="true"></span>
        <span class="name">Vintage Crest</span>
      </div>
    </section>

    <section class="card card-back" aria-label="Rückseite">
      <div class="back-panel">
        <span class="name">Vintage Crest</span>
      </div>
      <div class="gold-bar" aria-hidden="true"></div>
      <div class="contact">
        <h1 class="person">Markus<br>Wendler</h1>
        <p class="role">Owner</p>
        <ul class="details">
          <li>+43 670 19 27 468</li>
          <li>Sales@vintage-crest-autos.example</li>
          <li>Salzburg</li>
        </ul>
      </div>
    </section>
  </main>
</body>
</html>
```